I need a new business card design for my pharmacy.

I need a business card design. I will include my logo.
The card needs to be readable. I prefer to have my logo on one side along with my website, the other side includes the other information. Please use combination of black, neon green, white, and silver. This needs to catch the eye but yet be clearly visible and legible. Thanks

Industry/Entity Type

Pharmacy

Contact Information for Business Card

It needs to have the following information listed:
Mel's Apothecary Owner/Pharm D.
7134 North Brook Lane
Sioux Falls, SD 57231
Phone 605-318-6207
Fax 605-318-6209
email: mel@melsapothecary-example.com
www.melsapothecary-example.com
Store hours Monday-Friday 8 am- 7 pm
Saturday 8 am- 12 pm
Sunday Closed
Please utilize the colors black, white, and neon green, maybe silver.

Requirements
Must have
• It needs to be easily readable!
Nice to have
• It should catch the eye.
Should not have
• Do not use any other colors except listed: black, neon green, white, & silver.

```html
<!DOCTYPE html>
<html lang="en">
<head>
<meta charset="utf-8">
<title>Mel's Apothecary – Business Card</title>
<link rel="stylesheet" href="https://fonts.googleapis.com/css2?family=Lato:wght@300;400;700&display=swap">
<style>
  :root {
    --page: #e9e9e7;
    --card: #ffffff;
    --ink: #2e2e2e;
    --ink-soft: #4a4a4a;
    --neon: #8ccc2e;
    --black: #1c1c1c;
    --silver: #d2d2d2;
    --silver-text: #e4e4e4;
  }
  * { margin: 0; padding: 0; box-sizing: border-box; }
  html, body {
    width: 1200px; height: 1023px; overflow: hidden;
    background: var(--page);
    font-family: "Lato", sans-serif;
  }
  .card {
    position: absolute; left: 150px; top: 254px;
    width: 900px; height: 514px;
    background: var(--card);
    box-shadow: 0 10px 30px rgba(0,0,0,.18);
    overflow: hidden;
  }
  .card-art { position: absolute; inset: 0; }
  .brand-mark {
    position: absolute; left: 52px; top: 58px;
    width: 34px; height: 34px; border-radius: 50%;
    background: var(--neon);
  }
  .brand-divider {
    position: absolute; left: 112px; top: 40px;
    width: 2px; height: 84px; background: var(--ink);
  }
  .brand-name {
    position: absolute; left: 136px; top: 46px;
    font-size: 50px; font-weight: 700; letter-spacing: -1px;
    color: var(--ink);
  }
  .feature-name {
    position: absolute; right: 56px; top: 170px;
    font-size: 40px; font-weight: 700; color: var(--silver-text);
  }
  .store-hours {
    position: absolute; right: 58px; top: 236px;
    text-align: right; list-style: none;
    font-size: 17px; font-weight: 400; color: var(--ink-soft);
    line-height: 26px;
  }
  .store-hours .hours-title {
    font-weight: 700; color: var(--neon); font-size: 17px;
  }
  .holder { position: absolute; left: 110px; top: 160px; }
  .holder-name { font-size: 34px; font-weight: 400; color: var(--ink); }
  .holder-title { font-size: 21px; font-weight: 300; color: var(--neon); margin-top: 2px; }
  .contact-list {
    position: absolute; left: 110px; top: 262px;
    list-style: none;
  }
  .contact-list li {
    display: flex; align-items: center; gap: 18px;
    font-size: 22px; font-weight: 400; color: var(--ink-soft);
    height: 40px;
  }
  .contact-list svg { width: 22px; height: 22px; flex: none; }
  .address {
    position: absolute; left: 52px; top: 432px;
    display: flex; align-items: center; gap: 14px;
    font-size: 21px; color: #ffffff;
  }
  .address svg { width: 18px; height: 22px; }
  .website {
    position: absolute; right: 28px; top: 436px;
    font-size: 16px; font-weight: 300; color: var(--silver-text);
  }
</style>
</head>
<body>
  <article class="card">
    <svg class="card-art" viewBox="0 0 900 514" aria-hidden="true">
      <rect class="band-neon" x="0" y="416" width="580" height="60" fill="var(--neon)"/>
      <path class="band-black" d="M0 476 H540 Q552 476 556 464 L564 432 Q568 418 582 418 H900 V514 H0 Z" fill="var(--black)"/>
    </svg>

    <span class="brand-mark"></span>
    <span class="brand-divider"></span>
    <h1 class="brand-name">Mel's Apothecary</h1>
    <p class="feature-name">Mel's Apothecary</p>

    <ul class="store-hours">
      <li class="hours-title">Store Hours</li>
      <li>Mon–Fri 8 am – 7 pm</li>
      <li>Saturday 8 am – 12 pm</li>
      <li>Sunday Closed</li>
    </ul>

    <div class="holder">
      <p class="holder-name">Mel Harrow</p>
      <p class="holder-title">Owner/Pharm D.</p>
    </div>

    <ul class="contact-list">
      <li>
        <svg viewBox="0 0 24 24" fill="none" stroke="var(--neon)" stroke-width="2"><path d="M5 3h4l2 5-3 2a12 12 0 0 0 6 6l2-3 5 2v4a2 2 0 0 1-2 2A18 18 0 0 1 3 5a2 2 0 0 1 2-2z"/></svg>
        605-318-6207
      </li>
      <li>
        <svg viewBox="0 0 24 24" fill="none" stroke="var(--neon)" stroke-width="2"><rect x="6" y="3" width="12" height="6"/><rect x="3" y="9" width="18" height="9" rx="1"/><rect x="7" y="15" width="10" height="6"/></svg>
        605-318-6209
      </li>
      <li>
        <svg viewBox="0 0 24 24" fill="none" stroke="var(--neon)" stroke-width="2"><rect x="3" y="5" width="18" height="14"/><path d="M3 5l9 8 9-8"/></svg>
        mel@melsapothecary-example.com
      </li>
    </ul>

    <p class="address">
      <svg viewBox="0 0 18 22" fill="#ffffff"><path d="M9 0a8 8 0 0 1 8 8c0 6-8 14-8 14S1 14 1 8a8 8 0 0 1 8-8zm0 5a3 3 0 1 0 0 6 3 3 0 0 0 0-6z"/></svg>
      7134 North Brook Lane, Sioux Falls, SD 57231
    </p>
    <p class="website">www.melsapothecary-example.com</p>
  </article>
</body>
</html>
```